First Aid Training business needs business card design

We would like a double sided business card designed for a first aid training business - Brindlewood First Aid. We provide first aid training and , WHS (work, health and safety) training.

The attached word document contains the key information we would like on each side of the business card.

Final design needs to be delivered in print ready format, along with the original file.

```html
<!DOCTYPE html>
<html lang="en">
<head>
<meta charset="utf-8">
<title>Brindlewood First Aid – Business Card</title>
<link rel="stylesheet" href="https://fonts.googleapis.com/css2?family=Montserrat:wght@600&family=Poppins:wght@400;600;700&display=swap">
<style>
  :root {
    --brand-red: #ff0000;
    --deep-black: #000000;
    --paper-white: #ffffff;
    --ink-dark: #1f1f1f;
    --ink-grey: #3c3c3c;
    --edge-grey: #9a9a9a;
    --backdrop: #111111;
  }
  html, body {
    margin: 0;
    padding: 0;
    width: 1200px;
    height: 1099px;
    overflow: hidden;
    background: var(--backdrop);
  }
  .board {
    position: relative;
    width: 1200px;
    height: 1099px;
  }
  .card {
    position: absolute;
    left: 190px;
    width: 820px;
    height: 468px;
    display: block;
  }
  .card--front { top: 60px; }
  .card--back { top: 571px; }
  .wordmark { font-family: "Montserrat", sans-serif; font-weight: 600; }
  .body-text { font-family: "Poppins", sans-serif; }
  .fill-red { fill: var(--brand-red); }
  .fill-black { fill: var(--deep-black); }
  .fill-white { fill: var(--paper-white); }
  .name-first { font-weight: 700; fill: var(--brand-red); }
  .name-last { font-weight: 400; fill: var(--ink-dark); }
  .role { font-weight: 400; fill: var(--ink-grey); }
  .services { font-weight: 600; fill: var(--brand-red); }
  .contact { font-weight: 400; fill: var(--ink-dark); }
  .offer-title { font-weight: 600; fill: var(--ink-dark); }
  .offer-item { font-weight: 400; fill: var(--ink-dark); }
</style>
</head>
<body>
<main class="board">

  <!-- Front side -->
  <svg class="card card--front" viewBox="0 0 800 457" xmlns="http://www.w3.org/2000/svg" aria-label="Front of business card">
    <rect class="fill-red" x="0" y="0" width="800" height="457"/>
    <polygon class="fill-black" points="0,413 330,413 405,385 478,413 800,413 800,457 0,457"/>
    <polyline points="0,407 328,407 405,378 480,407 800,407" fill="none" stroke="var(--paper-white)" stroke-width="6"/>
    <g class="brand-lockup">
      <circle class="fill-white" cx="228" cy="218" r="62"/>
      <text class="wordmark fill-white" x="310" y="212" font-size="52">BRINDLEWOOD</text>
      <text class="wordmark fill-white" x="312" y="254" font-size="28">FIRST AID TRAINING</text>
    </g>
  </svg>

  <!-- Back side -->
  <svg class="card card--back" viewBox="0 0 800 457" xmlns="http://www.w3.org/2000/svg" aria-label="Back of business card">
    <rect class="fill-white" x="0" y="0" width="800" height="457"/>
    <polygon class="fill-red" points="0,0 88,0 88,148 138,225 88,302 85,457 0,457"/>
    <polygon class="fill-red" points="800,0 712,0 712,148 662,225 712,302 715,457 800,457"/>
    <polyline points="90,0 90,148 140,225 90,302 87,457" fill="none" stroke="var(--edge-grey)" stroke-width="4"/>
    <polyline points="710,0 710,148 660,225 710,302 713,457" fill="none" stroke="var(--edge-grey)" stroke-width="4"/>

    <g class="brand-lockup">
      <circle class="fill-red" cx="280" cy="85" r="44"/>
      <text class="wordmark" x="340" y="86" font-size="38" fill="var(--ink-dark)">BRINDLEWOOD</text>
      <text class="wordmark" x="341" y="114" font-size="20" fill="var(--ink-dark)">FIRST AID TRAINING</text>
    </g>

    <g class="person body-text" text-anchor="middle">
      <text x="400" y="226" font-size="26"><tspan class="name-first">DANA</tspan><tspan class="name-last"> MORROW</tspan></text>
      <text class="role" x="400" y="250" font-size="18">President</text>
    </g>

    <g class="contact-block body-text">
      <text class="services" x="105" y="356" font-size="16">First Aid Training, WHS Training</text>
      <path class="fill-red" d="M109,369 l3,-1 2,4 -2,1.5 q1.5,3 4,4.5 l1.5,-2 4,2 -1,3 q-8,0 -11.5,-12z"/>
      <text class="contact" x="124" y="380" font-size="12">0412 555 018</text>
      <rect class="fill-red" x="108" y="393" width="12" height="8" rx="1"/>
      <polyline points="108,393 114,398 120,393" fill="none" stroke="var(--paper-white)" stroke-width="1"/>
      <text class="contact" x="124" y="401" font-size="12">help@brindlewoodfirstaid.com.au</text>
      <g fill="none" stroke="var(--brand-red)" stroke-width="1.2">
        <circle cx="114" cy="417" r="5.5"/>
        <ellipse cx="114" cy="417" rx="2.3" ry="5.5"/>
        <line x1="108.5" y1="417" x2="119.5" y2="417"/>
      </g>
      <text class="contact" x="124" y="421" font-size="12">brindlewoodfirstaid.com.au</text>
    </g>

    <g class="offer-block body-text">
      <text class="offer-title" x="423" y="356" font-size="13.5">Onsite Training – We can come to you</text>
      <text class="offer-item" x="423" y="378" font-size="14">·Time efficient</text>
      <text class="offer-item" x="423" y="400" font-size="14">·Cost effective</text>
      <text class="offer-item" x="423" y="422" font-size="14">·Minimise downtime for your team</text>
    </g>
  </svg>

</main>
</body>
</html>
```